Menu Board and Flyer for a Poke Restaurant

We need for our new Menu board for a Poke restaurant. There will be 2 separate boards. 1 Board for Speciality items, the second for "Build your Own". The menu boards will be installed on a wall.

The first board is going to be 36 W x 48 H inches. The second board will be 72 W x 48 H inches.

I would also like to consolidate the board into a one Page menu flyer that can be printed on an 11 inches x 14 inches Page.

The goal is to have customers focus on the ease of ordering.
We have attached a sample design idea for reference and our logo options. Including the logo is optional.

I have included some sample menus by other companies as attachment and referance.

Files need to include any special fonts used in the design.

Target Market(s)

Young Professionals who love eating healthy, trendy, delicious new food options.

Industry/Entity Type

Fast Food Restaurant

Font styles to use
Serif
Sans Serif

Requirements
Must have
• Simple
• Clean design - NOT busy
• Fun
• Easy to follow
• Highlight a step by step ordering process.
• Light background color
• Files need to include any special fonts used in the design.
Should not have
• script fonts

```html
<!DOCTYPE html>
<html lang="en">
<head>
<meta charset="utf-8">
<title>Coastline Poke House – Menu Boards</title>
<link rel="stylesheet" href="https://fonts.googleapis.com/css2?family=Oswald:wght@300;400;600;700&family=PT+Sans+Narrow:wght@400;700&family=Kalam:wght@400&display=swap">
<style>
:root{
  --stage:#6b6d70;
  --teal:#0f7e86;
  --teal-dark:#0b6a72;
  --sky:#8fd0ee;
  --sky-pale:#cfeaf7;
  --ink:#1f1f1f;
  --green:#2fae4a;
  --white:#ffffff;
  --wave-a:#bfe3f2;
  --wave-b:#6cbfc6;
}
*{margin:0;padding:0;box-sizing:border-box}
html,body{width:1200px;height:598px;overflow:hidden;background:var(--stage)}
body{position:relative;font-family:"PT Sans Narrow",sans-serif;color:var(--ink)}
.board{position:absolute;background:var(--white);overflow:hidden;box-shadow:8px 10px 14px rgba(0,0,0,.35)}
.abs{position:absolute}
.vertical{writing-mode:vertical-rl;transform:rotate(180deg);white-space:nowrap}

/* specialties board */
.specialties{left:80px;top:77px;width:310px;height:413px}
.specialties .header{left:0;top:0;width:310px;height:58px;background:var(--teal);color:var(--white);
  font:400 31px/58px "Oswald",sans-serif;text-align:center;letter-spacing:.5px}
.specialties .side{left:0;top:58px;width:48px;height:182px;background:linear-gradient(#eaf6fb,var(--sky))}
.specialties .side span{position:absolute;left:12px;top:12px;font:700 18px/1 "Oswald",sans-serif;color:var(--ink)}
.dish{width:72px;height:72px;border-radius:50%;background:var(--teal);color:var(--white);
  text-align:center;font:400 15px/1.05 "Oswald",sans-serif;display:flex;flex-direction:column;align-items:center;justify-content:center;gap:2px}
.dish .art{width:26px;height:10px;border-radius:3px;background:#9bcf6a;opacity:.85}
.style-head{white-space:nowrap}
.style-head .choose-small{display:block;font:700 11px/1 "Oswald",sans-serif;color:var(--green);transform:scaleX(.8);transform-origin:left}
.style-head .style-big{display:block;font:700 46px/1 "Oswald",sans-serif;color:var(--teal);transform:scaleX(.6);transform-origin:left}
.item{white-space:nowrap}
.item b{display:block;font:700 15px/1.1 "PT Sans Narrow",sans-serif}
.item small{display:block;font:400 11px/1.25 "PT Sans Narrow",sans-serif}
.brand{font:400 14px/15px "PT Sans Narrow",sans-serif;color:var(--teal);text-align:center;letter-spacing:.5px}
.waves{background:linear-gradient(180deg,var(--wave-a),var(--wave-b) 60%,var(--wave-a))}
.sticks{background:linear-gradient(170deg,transparent 40%,#3a3a3a 42%,#999 46%,transparent 48%)}

/* build board */
.build{left:483px;top:78px;width:623px;height:416px}
.build .header{left:0;top:0;width:623px;height:92px;background:var(--teal)}
.build .header .stripe{left:430px;top:0;width:80px;height:92px;background:var(--teal-dark);transform:skewX(-30deg)}
.build .fish{left:14px;top:30px;width:118px;height:40px;border-radius:50% 40% 40% 50%;background:#5fb3c7;opacity:.8}
.build .title{left:52px;top:26px;font:400 36px/1 "Oswald",sans-serif;color:var(--white);letter-spacing:.3px;white-space:nowrap}
.badge{left:390px;top:12px;width:108px;height:108px;border-radius:50%;background:var(--white);border:3px solid var(--teal);
  display:flex;align-items:center;justify-content:center;text-align:center}
.badge span{font:700 14px/1.15 "PT Sans Narrow",sans-serif;color:var(--teal)}
.build .side{left:0;top:92px;width:107px;height:324px;background:linear-gradient(var(--sky),var(--sky-pale))}
.step-one{left:36px;top:90px;width:38px;height:38px;border-radius:50%;background:var(--white);
  font:600 20px/38px "Oswald",sans-serif;text-align:center}
.build-style{left:18px;top:134px;width:76px;text-align:center;white-space:nowrap}
.build-style .choose-small{display:block;font:700 12px/1 "Oswald",sans-serif;color:var(--ink);transform:scaleX(.85)}
.build-style .style-big{display:block;font:700 44px/1 "Oswald",sans-serif;color:var(--ink);transform:scaleX(.8)}
.lead{left:128px;top:112px;font:400 23px/1 "Kalam",sans-serif;white-space:nowrap}
.step{width:36px;height:36px;background:var(--teal);color:var(--white);font:600 21px/36px "Oswald",sans-serif;text-align:center}
.col-label{left:0;top:40px;display:flex;flex-direction:column;align-items:flex-start}
.col-label .choose-small{font:700 7px/1 "Oswald",sans-serif;color:var(--green);white-space:nowrap;margin-bottom:2px}
.col-label .word{font:700 30px/1 "Oswald",sans-serif;color:var(--teal)}
.list{list-style:none;font:700 12px/16.6px "PT Sans Narrow",sans-serif;white-space:nowrap}
</style>
</head>
<body>

<section class="board specialties">
  <h1 class="abs header">HOUSE SPECIALTIES</h1>
  <div class="abs side"><span class="vertical">CHOOSE A SPECIALTY</span></div>
  <div class="abs dish" style="left:48px;top:67px">LAVA<div class="art" role="img" aria-label="volcano icon" style="background:#8a5a2b"></div>HOT</div>
  <div class="abs dish" style="left:132px;top:67px">CLASSIC<div class="art" role="img" aria-label="hibiscus flower icon" style="background:#e0399a"></div>HAWAIIN</div>
  <div class="abs dish" style="left:216px;top:67px">SWEET<div class="art" role="img" aria-label="chili pepper icon" style="background:#d9362b"></div>SPICY</div>
  <div class="abs dish" style="left:48px;top:151px">WASABI<div class="art" role="img" aria-label="wasabi root icon"></div>LOVER</div>
  <div class="abs dish" style="left:132px;top:151px">GINGER<div class="art" role="img" aria-label="ginger root icon" style="background:#c79a5a"></div>GINGER</div>
  <div class="abs dish" style="left:216px;top:151px">CRAZY<div class="art" role="img" aria-label="cabbage leaf icon"></div>KIMCHI</div>

  <div class="abs style-head" style="left:16px;top:248px">
    <span class="choose-small">CHOOSE YOUR</span>
    <span class="style-big">STYLE</span>
  </div>
  <div class="abs item" style="left:96px;top:243px"><b>Classic Bowl</b><small>Regular or Large</small></div>
  <div class="abs item" style="left:196px;top:243px"><b>Crunchy Bowl</b><small>One Size, Tostada Style</small></div>
  <div class="abs item" style="left:96px;top:282px"><b>Surfer Style</b><small>Poke Served Taco Style</small></div>
  <div class="abs item" style="left:196px;top:282px"><b>Just Poke (1lb)</b><small>No Base -1lb of Your<br>Favorite Poke</small></div>
  <div class="abs brand" style="left:88px;top:326px;width:100px">Coastline<br>Poke House</div>
  <div class="abs waves" role="img" aria-label="ocean wave pattern" style="left:0;top:362px;width:310px;height:51px"></div>
  <div class="abs sticks" role="img" aria-label="chopsticks" style="left:130px;top:355px;width:180px;height:50px"></div>
</section>

<section class="board build">
  <div class="abs header">
    <div class="abs stripe"></div>
    <div class="abs fish" role="img" aria-label="tuna silhouette"></div>
    <h1 class="abs title">BUILD YOUR OWN POKE</h1>
  </div>
  <div class="abs sticks" role="img" aria-label="chopsticks" style="left:360px;top:0;width:263px;height:170px"></div>
  <div class="abs badge"><span>Coastline<br>Poke House</span></div>

  <div class="abs side"></div>
  <div class="abs step-one">1.</div>
  <div class="abs build-style">
    <span class="choose-small">CHOOSE YOUR</span>
    <span class="style-big">STYLE</span>
  </div>
  <div class="abs item" style="left:12px;top:210px"><b>Classic Bowl</b><small>Regular or Large</small></div>
  <div class="abs item" style="left:12px;top:252px"><b>Crunchy Bowl</b><small>One Size, Tostada Style</small></div>
  <div class="abs item" style="left:12px;top:294px"><b>Surfer Style</b><small>Poke Served Taco Style</small></div>
  <div class="abs item" style="left:12px;top:336px"><b>Just Poke <span style="font-size:12px">(1lb)</span></b><small>No Base -1lb of Your<br>Favorite Poke</small></div>

  <p class="abs lead">Choose One of Each</p>

  <div class="abs waves" role="img" aria-label="ocean wave pattern" style="left:107px;top:354px;width:516px;height:62px"></div>

  <div class="abs" style="left:127px;top:154px">
    <div class="step">2.</div>
    <div class="abs col-label"><span class="choose-small">CHOOSE YOUR</span><span class="word vertical">FISH</span></div>
  </div>
  <ul class="abs list" style="left:171px;top:156px"><li>Ahi</li><li>Tuna</li><li>Salmon</li><li>Hamachi</li><li>Spicy Tuna</li><li>Shrimp</li><li>Scallop</li></ul>

  <div class="abs" style="left:237px;top:154px">
    <div class="step">3.</div>
    <div class="abs col-label"><span class="choose-small">CHOOSE YOUR</span><span class="word vertical">TOPPINGS</span></div>
  </div>
  <ul class="abs list" style="left:281px;top:156px"><li>Crispy Onion</li><li>Green Onion</li><li>Sweet Onion</li><li>Masago</li><li>Cilantro</li><li>Cucumber</li><li>Corn</li><li>Coconut Flakes</li><li>Hawaiian Sea Salt</li><li>Chili Flakes</li><li>Ogo</li><li>Furikake</li><li>Panko</li><li>Sesame Seed</li><li>Avacado</li></ul>

  <div class="abs" style="left:371px;top:154px">
    <div class="step">4.</div>
    <div class="abs col-label"><span class="choose-small">CHOOSE YOUR</span><span class="word vertical">SAUCE</span></div>
  </div>
  <ul class="abs list" style="left:415px;top:156px"><li>Sesame Shoyu</li><li>Sriracha Aioli</li><li>Ponzu</li><li>Sweet Shoyu</li><li>Wasabi Shoyu</li><li>Sweet Chili</li><li>Chili Lime</li><li>Ginger-Scallion</li><li>Wasabi Creme</li></ul>

  <div class="abs" style="left:501px;top:154px">
    <div class="step">5.</div>
    <div class="abs col-label"><span class="choose-small">CHOOSE YOUR</span><span class="word vertical">BASE</span></div>
  </div>
  <ul class="abs list" style="left:545px;top:156px"><li>White Rice</li><li>Brown Rice</li><li>Black Rice</li><li>Mixed Greens</li></ul>
</section>

</body>
</html>
```